COVID-19 Accredited CME Impact Infographic

We want an infographic showing how much COVID-19 Continuing Medical Education we have accredited and its impact. Our website is at https://med.halvering.edu/cme/COVID19/education.html The attached document is intended to simply show the elements. You have complete freedom on design. We will be updating the numbers weekly so it is important that we have the files so that we can update it. This can be done in powerpoint, publisher, word, in-design, illustrator. Don't use crazy fonts that we wont have.

Target Market(s)

Internal to Halvering. We just want to show the impact of our work

Industry/Entity Type

Education

Requirements
Must have
• We must be able to update the numbers ourselves.

See attached document for the pieces that we want.

The sizes of the numbers in the attached are based on importance to us.
Nice to have
• Not mandatory but try to use these colors. https://med.halvering.edu/identity/color-palette.html

I was thinking that perhaps the big number could be done in traditional train. Like this: https://www.pictovane.com/image-illustration/flip-board-under-constuction-page-isolated-8803617452

```html
<!DOCTYPE html>
<html lang="en">
<head>
<meta charset="utf-8">
<title>COVID-19 CME Impact</title>
<link rel="stylesheet" href="https://fonts.googleapis.com/css2?family=Lato:wght@700;900&family=Montserrat:wght@600&display=swap">
<style>
  :root {
    --cardinal: #7a1022;
    --cardinal-soft: #9a3a48;
    --icon-red: #c00000;
    --ink: #0d0d0d;
    --paper: #ffffff;
    --paper-shade: #e4e5e7;
    --map-tone: #dcdde0;
    --tile-dark: #2b2b2b;
    --tile-mid: #4a4a4a;
  }
  * { margin: 0; padding: 0; box-sizing: border-box; }
  html, body { width: 1200px; height: 675px; overflow: hidden; }
  body { font-family: "Lato", Arial, sans-serif; color: var(--ink); }

  .infographic {
    position: relative; width: 1200px; height: 675px; overflow: hidden;
    background: linear-gradient(90deg, var(--paper) 35%, var(--paper-shade) 100%);
  }
  .world-map {
    position: absolute; left: 412px; top: 160px; width: 660px; height: 365px;
    border-radius: 50%;
    background: radial-gradient(ellipse at center, var(--map-tone) 0%, rgba(220,221,224,0.5) 45%, rgba(220,221,224,0) 72%);
  }
  .title-panel { position: absolute; left: 0; top: 0; width: 480px; height: 675px; }
  .virus-decor {
    position: absolute; left: -30px; top: 425px; width: 150px; height: 190px;
    border-radius: 50%;
    background: radial-gradient(circle, var(--cardinal-soft) 0%, rgba(154,58,72,0.4) 55%, rgba(154,58,72,0) 72%);
  }
  .title {
    position: absolute; left: 0; top: 0;
    font-family: "Montserrat", Arial, sans-serif; font-weight: 600;
    font-size: 110px; line-height: 1; color: var(--paper); letter-spacing: -1px;
  }
  .title span { position: absolute; white-space: nowrap; }
  .title .t1 { left: 64px; top: 24px; }
  .title .t2 { left: 228px; top: 142px; }
  .title .t3 { left: 92px; top: 254px; }

  .brand {
    position: absolute; right: 8px; top: 12px;
    font-family: "Lato", Arial, sans-serif; font-weight: 700;
    font-size: 22px; color: var(--cardinal); display: flex; align-items: center; gap: 6px;
  }
  .brand-mark { width: 16px; height: 16px; background: var(--cardinal); }

  .stat { position: absolute; }
  .stat-icon { position: absolute; }
  .stat-label { position: absolute; font-weight: 900; font-size: 21px; white-space: nowrap; }
  .stat-value { position: absolute; font-weight: 900; white-space: nowrap; line-height: 1; }

  .activities-label {
    position: absolute; left: 710px; top: 486px;
    font-weight: 900; font-size: 42px; white-space: nowrap;
  }
  .flip-tile {
    position: absolute; top: 478px; width: 126px; height: 161px; border-radius: 8px;
    background: linear-gradient(180deg, var(--tile-mid) 0%, var(--tile-dark) 49%, #111 50%, var(--tile-dark) 51%, var(--tile-mid) 100%);
    border: 3px solid #1a1a1a;
    color: var(--paper); font-family: "Lato", Arial, sans-serif; font-weight: 900;
    font-size: 140px; line-height: 155px; text-align: center;
  }
  .flip-tile::before, .flip-tile::after {
    content: ""; position: absolute; top: 70px; width: 6px; height: 16px; background: #888; border-radius: 1px;
  }
  .flip-tile::before { left: -4px; }
  .flip-tile::after { right: -4px; }
</style>
</head>
<body>
<main class="infographic">
  <div class="world-map" role="img" aria-label="Faint world map in the background"></div>

  <section class="title-panel">
    <svg width="480" height="675" viewBox="0 0 480 675" aria-hidden="true">
      <polygon points="0,0 478,0 220,675 0,675" fill="var(--cardinal)"/>
    </svg>
    <div class="virus-decor" role="img" aria-label="Faint coronavirus particle illustration"></div>
    <h1 class="title"><span class="t1">COVID</span><span class="t2">-19</span><span class="t3">CME</span></h1>
  </section>

  <div class="brand"><span class="brand-mark"></span>Halvering Medicine</div>

  <!-- states -->
  <svg class="stat-icon" style="left:553px;top:70px" width="58" height="90" viewBox="0 0 58 90" aria-hidden="true">
    <g fill="none" stroke="var(--icon-red)" stroke-width="3">
      <circle cx="30" cy="32" r="22"/>
      <ellipse cx="30" cy="32" rx="10" ry="22"/>
      <line x1="8" y1="32" x2="52" y2="32"/>
      <line x1="12" y1="20" x2="48" y2="20"/>
      <line x1="12" y1="44" x2="48" y2="44"/>
      <path d="M6 14 A30 30 0 0 0 40 62"/>
      <line x1="27" y1="62" x2="27" y2="78"/>
    </g>
    <rect x="12" y="78" width="30" height="5" fill="var(--icon-red)"/>
  </svg>
  <div class="stat-label" style="left:616px;top:78px"># of states</div>
  <div class="stat-value" style="left:613px;top:108px;font-size:60px">26</div>

  <!-- countries -->
  <svg class="stat-icon" style="left:788px;top:86px" width="74" height="74" viewBox="0 0 74 74" aria-hidden="true">
    <g fill="none" stroke="var(--icon-red)" stroke-width="5">
      <circle cx="37" cy="37" r="33"/>
      <ellipse cx="37" cy="37" rx="14" ry="33"/>
      <line x1="4" y1="37" x2="70" y2="37"/>
      <path d="M10 20 H64 M10 54 H64"/>
    </g>
  </svg>
  <div class="stat-label" style="left:872px;top:82px"># of Countries</div>
  <div class="stat-value" style="left:871px;top:108px;font-size:60px">12</div>

  <!-- live learners -->
  <svg class="stat-icon" style="left:420px;top:206px" width="82" height="85" viewBox="0 0 82 85" aria-hidden="true">
    <circle cx="41" cy="20" r="19" fill="var(--icon-red)"/>
    <path d="M4 85 V62 Q4 44 22 44 H60 Q78 44 78 62 V85 Z" fill="var(--icon-red)"/>
  </svg>
  <div class="stat-label" style="left:525px;top:212px"># of live Learners</div>
  <div class="stat-value" style="left:510px;top:238px;font-size:72px">23,098</div>

  <!-- CME learners -->
  <svg class="stat-icon" style="left:778px;top:214px" width="82" height="85" viewBox="0 0 82 85" aria-hidden="true">
    <circle cx="41" cy="20" r="19" fill="var(--icon-red)"/>
    <path d="M4 85 V62 Q4 44 22 44 H60 Q78 44 78 62 V85 Z" fill="var(--icon-red)"/>
  </svg>
  <div class="stat-label" style="left:872px;top:214px"># of CME Learners</div>
  <div class="stat-value" style="left:870px;top:240px;font-size:72px">5,879</div>

  <!-- on-demand views -->
  <svg class="stat-icon" style="left:553px;top:356px" width="78" height="68" viewBox="0 0 78 68" aria-hidden="true">
    <circle cx="26" cy="26" r="21" fill="none" stroke="var(--icon-red)" stroke-width="6"/>
    <path d="M14 22 A13 13 0 0 1 26 13" fill="none" stroke="var(--icon-red)" stroke-width="3"/>
    <line x1="42" y1="41" x2="72" y2="63" stroke="var(--icon-red)" stroke-width="10" stroke-linecap="round"/>
  </svg>
  <div class="stat-label" style="left:624px;top:342px">#of total on-demand views</div>
  <div class="stat-value" style="left:632px;top:372px;font-size:60px">1,209,987</div>

  <!-- activities -->
  <div class="flip-tile" style="left:443px">2</div>
  <div class="flip-tile" style="left:568px">6</div>
  <div class="activities-label"># of activities</div>
</main>
</body>
</html>
```